KVT Building And Maintenance

Need a very professional looking double sided Buisiness card with all my details phone number, name, email, license number.

Target Market(s)

construction industry

Industry/Entity Type

building

Contact Information for Business Card

Name Dale Pemberton. Email Address Info@KVTBuilding.com.au mobile number 0452918736 licence number 671093D. web site

```html
<!DOCTYPE html>
<html lang="en">
<head>
<meta charset="utf-8">
<title>KVT Building And Maintenance – Business Card</title>
<link rel="stylesheet" href="https://fonts.googleapis.com/css2?family=Exo+2:wght@400;500;700;800&display=swap">
<style>
  :root {
    --stage: #1c1c1e;
    --navy: #040e20;
    --blue: #4a9fe0;
    --ink: #3d3e42;
    --rule: #9a9a9a;
    --paper: #ffffff;
  }
  * { box-sizing: border-box; margin: 0; padding: 0; }
  html, body {
    width: 1200px; height: 1015px; overflow: hidden;
    background: var(--stage);
    font-family: "Exo 2", sans-serif;
  }
  .canvas {
    width: 1200px; height: 1015px;
    display: flex; flex-direction: column; align-items: center; justify-content: center;
    gap: 56px;
  }
  .card {
    position: relative;
    width: 640px; height: 366px;
    overflow: hidden;
    box-shadow: 0 18px 40px rgba(0,0,0,.55);
  }

  /* Back side */
  .card--back { background: var(--navy); }
  .card--back .brand {
    position: absolute; left: 0; right: 0; top: 118px;
    display: flex; align-items: center; justify-content: center; gap: 14px;
    color: var(--paper);
  }
  .brand__mark { width: 22px; height: 22px; background: var(--blue); }
  .brand__name {
    font-weight: 800; font-size: 30px; letter-spacing: 1.5px; text-transform: uppercase;
    line-height: 1.05;
  }
  .card--back .band {
    position: absolute; left: 0; right: 0; top: 250px; height: 42px;
    background: var(--blue);
    display: flex; align-items: center; justify-content: center;
    color: var(--paper); font-size: 19px; letter-spacing: .5px;
  }

  /* Front side */
  .card--front { background: var(--paper); }
  .front-brand {
    position: absolute; left: 44px; top: 120px; width: 250px;
    display: flex; align-items: center; gap: 12px;
  }
  .front-brand .brand__name { color: var(--ink); font-size: 24px; }
  .divider {
    position: absolute; left: 318px; top: 92px; width: 1px; height: 140px;
    background: var(--rule);
  }
  .contact { position: absolute; left: 344px; top: 92px; color: var(--ink); }
  .contact__name {
    font-weight: 800; font-size: 25px; letter-spacing: 1px; text-transform: uppercase;
    margin-bottom: 14px;
  }
  .contact__list { list-style: none; }
  .contact__item {
    display: flex; align-items: center; gap: 10px;
    font-size: 16.5px; line-height: 27px;
  }
  .contact__item svg { width: 17px; height: 17px; flex: none; }
  .accent { color: var(--blue); }
  .strip-blue {
    position: absolute; left: 0; bottom: 0; width: 430px; height: 22px;
    background: var(--blue);
  }
  .licence {
    position: absolute; right: 0; bottom: 0; width: 240px; height: 52px;
    background: var(--navy);
    clip-path: polygon(12px 0, 100% 0, 100% 100%, 0 100%);
    display: flex; align-items: center; justify-content: center; gap: 6px;
    font-size: 18px; color: var(--paper);
  }
  .licence__label { color: var(--blue); }
</style>
</head>
<body>
<main class="canvas">

  <section class="card card--back" aria-label="Business card back">
    <div class="brand">
      <span class="brand__mark"></span>
      <span class="brand__name">KVT Building<br>And Maintenance</span>
    </div>
    <div class="band">www.KVTBuilding.com.au</div>
  </section>

  <section class="card card--front" aria-label="Business card front">
    <div class="front-brand">
      <span class="brand__mark"></span>
      <span class="brand__name">KVT Building<br>And Maintenance</span>
    </div>
    <div class="divider"></div>
    <div class="contact">
      <h1 class="contact__name">Dale Pemberton</h1>
      <ul class="contact__list">
        <li class="contact__item">
          <svg viewBox="0 0 24 24" fill="#4a9fe0" aria-hidden="true"><path d="M6.6 10.8a15.1 15.1 0 0 0 6.6 6.6l2.2-2.2c.3-.3.7-.4 1-.2 1.1.4 2.3.6 3.6.6.6 0 1 .4 1 1V20c0 .6-.4 1-1 1A17 17 0 0 1 3 4c0-.6.4-1 1-1h3.5c.6 0 1 .4 1 1 0 1.3.2 2.5.6 3.6.1.3 0 .7-.2 1z"/></svg>
          <span>0452918736</span>
        </li>
        <li class="contact__item">
          <svg viewBox="0 0 24 24" fill="#4a9fe0" aria-hidden="true"><path d="M2 5h20v14H2z" opacity=".35"/><path d="M2 5l10 8 10-8v2l-10 8L2 7z"/></svg>
          <span>Info@KVTBuilding.com.au</span>
        </li>
        <li class="contact__item">
          <svg viewBox="0 0 24 24" fill="none" stroke="#4a9fe0" stroke-width="2" aria-hidden="true"><circle cx="12" cy="12" r="9"/><path d="M3 12h18M12 3c3 3 3 15 0 18M12 3c-3 3-3 15 0 18"/></svg>
          <span>www.<span class="accent">KVTBuilding</span>.com.au</span>
        </li>
      </ul>
    </div>
    <div class="strip-blue"></div>
    <div class="licence"><span class="licence__label">Licence No.</span><span>671093D</span></div>
  </section>

</main>
</body>
</html>
```